Icon and color palette for a math game

We are in development of a mathematics game, and need a fresh and engaging icon and text logo (logotype/word mark) and splash screen. We would also like suggestions for a colour palette.

The main element in the project is the icon. We need an icon that says something about what the game is all about. We have uploaded a sketch for your inspiration.

The game is about challenging your friends to see who can create the most calculations based on numbers and operations (+ and -) that are presented to you. The name of the game is Tallyquarrel.

Attached are some images for inspiration:
- Home
- Game board
Updates

Project Deadline Extended
Reason: Deadline is extended due to christmas holidays. We'll be slow at responding the upcoming days.

Target Market(s)

Children and grown-ups that like to play games and challenge each other.

Requirements
Must have
• - iOS app icons
- Android app icons
- Windows phone app icons
- Text logo
- Splash screen (the screen that is shown while the game loads)
- Color palette
- Example of the two images attached with the new palette

```html
<!DOCTYPE html>
<html lang="en">
<head>
<meta charset="utf-8">
<title>Tallyquarrel – icon, splash and palette</title>
<link rel="stylesheet" href="https://fonts.googleapis.com/css2?family=Roboto:wght@300;400;500;700&display=swap">
<style>
  :root{
    --sky:#18c0ff;
    --sky-mid:#7cdbff;
    --sky-pale:#a8e7ff;
    --brick:#ce5753;
    --tangerine:#ed7e27;
    --canvas:#f2f2f2;
    --frame:#5f5f5f;
    --status:#1d2b33;
    --header:#3cc3f5;
    --board:#9edcf4;
    --card:#eeeeee;
    --card-line:#d6d6d6;
    --ink:#333333;
    --muted:#9a9a9a;
    --white:#ffffff;
  }
  *{box-sizing:border-box;margin:0;padding:0}
  html,body{width:1200px;height:1000px;overflow:hidden;background:var(--canvas)}
  body{position:relative;font-family:"Roboto",Arial,sans-serif;color:var(--ink)}
  .abs{position:absolute}

  /* status bar */
  .status-bar{position:absolute;left:0;right:0;top:0;background:var(--status);color:#cfd8dc;display:flex;align-items:center;font-weight:700}
  .status-bar .carrier{display:flex;align-items:flex-end;gap:1px}
  .status-bar .lock{position:absolute;left:50%;transform:translateX(-50%)}
  .status-bar .battery{position:absolute}

  /* app header */
  .app-header{position:absolute;left:0;right:0;background:linear-gradient(var(--sky-mid),var(--header));display:flex;align-items:center;color:var(--white)}
  .app-header .back{display:flex;align-items:center;font-weight:300}
  .app-header .wordmark{position:absolute;left:50%;transform:translateX(-50%);font-weight:700;white-space:nowrap}
  .app-header .compose{position:absolute}
  .board{position:absolute;left:0;right:0;bottom:0;background:var(--board)}
  .wordmark{color:var(--white);font-weight:700;font-family:"Roboto",Arial,sans-serif}

  /* zoom detail panel */
  .detail{left:0;top:0;width:527px;height:527px;border:4px solid var(--frame);border-left:none;border-top:none;background:var(--canvas)}
  .detail .divider{position:absolute;left:0;top:258px;width:523px;height:4px;background:var(--frame)}
  .detail-header{left:68px;top:20px;width:387px;height:238px;overflow:hidden;border-radius:8px 8px 0 0}
  .detail-splash{left:75px;top:262px;width:373px;height:261px;overflow:hidden;background:radial-gradient(circle at 30% 20%,var(--sky-pale),var(--sky) 70%)}
  .detail-splash .wordmark{position:absolute;left:0;right:0;top:102px;text-align:center;font-size:56px}

  .tab{position:absolute;height:20px;background:linear-gradient(var(--tangerine),#f6a043);clip-path:polygon(0 0,80% 0,100% 100%,0 100%)}
  .tab.red{background:linear-gradient(#e07a76,var(--brick))}
  .tab .clock{position:absolute;left:5px;top:3px;width:14px;height:14px;border-radius:50%;border:2px solid var(--white)}
  .row{position:absolute;background:var(--card);border-bottom:1px solid var(--card-line);display:flex;align-items:center}
  .avatar{border-radius:50%;background:#8a8f95;flex:none}
  .avatar.warm{background:#c98a4e}
  .row .name{font-weight:700;color:#444}
  .row .sub{color:var(--muted)}
  .row .chev{position:absolute;color:var(--brick)}

  /* splash screen */
  .splash{left:587px;top:108px;width:196px;height:476px;background:radial-gradient(circle at 30% 30%,var(--sky-pale),var(--sky) 70%)}
  .splash .wordmark{position:absolute;left:0;right:0;top:222px;text-align:center;font-size:27px}

  /* game list screen */
  .games{left:955px;top:105px;width:200px;height:485px;overflow:hidden}
  .games .group-line{position:absolute;left:20px;width:163px;height:2px}

  /* icon */
  .app-icon{left:126px;top:570px;width:292px;height:290px;border-radius:60px;background:linear-gradient(#4ccdf2,#0d9fdb)}

  /* palette */
  .palette-label{left:28px;top:920px;font-size:18px;line-height:24px;color:#333;text-align:center}
  .swatch{position:absolute;top:904px;width:52px;height:50px;border-radius:9px}
  .swatch-code{position:absolute;top:962px;font-size:17px;color:#333;width:90px;text-align:center}

  /* bottom header detail */
  .detail-bottom{left:633px;top:852px;width:462px;height:148px;overflow:hidden;border-radius:6px 6px 0 0}
</style>
</head>
<body>

<!-- detail panel -->
<section class="abs detail">
  <div class="abs detail-header">
    <div class="status-bar" style="height:38px;font-size:17px;padding-left:10px">
      <span class="carrier"><svg width="22" height="12" viewBox="0 0 22 12"><rect x="0" y="8" width="3" height="4" fill="#cfd8dc"/><rect x="5" y="6" width="3" height="6" fill="#cfd8dc"/><rect x="10" y="4" width="3" height="8" fill="#cfd8dc"/><rect x="15" y="2" width="3" height="10" fill="#cfd8dc"/></svg>CARRIER</span>
      <svg class="lock" width="14" height="18" viewBox="0 0 14 18"><path d="M3 8V5a4 4 0 0 1 8 0v3" fill="none" stroke="#cfd8dc" stroke-width="2"/><rect x="1" y="8" width="12" height="9" rx="1" fill="#cfd8dc"/></svg>
      <svg class="battery" style="right:12px" width="24" height="12" viewBox="0 0 24 12"><rect x="1" y="1" width="20" height="10" rx="1" fill="none" stroke="#cfd8dc" stroke-width="1.5"/><rect x="3" y="3" width="16" height="6" fill="#cfd8dc"/><rect x="22" y="4" width="2" height="4" fill="#cfd8dc"/></svg>
    </div>
    <div class="app-header" style="top:38px;height:72px;padding-left:12px">
      <span class="back" style="font-size:24px"><svg width="16" height="28" viewBox="0 0 16 28"><path d="M13 2 3 14l10 12" fill="none" stroke="#fff" stroke-width="3"/></svg>&nbsp;Back</span>
      <span class="wordmark" style="font-size:34px">Tallyquarrel</span>
      <svg class="compose" style="right:16px" width="28" height="30" viewBox="0 0 28 30"><path d="M18 4H2v24h20V12" fill="none" stroke="#fff" stroke-width="2"/><path d="M10 20l2-6 13-13 4 4-13 13z" fill="none" stroke="#fff" stroke-width="2"/></svg>
    </div>
    <div class="board" role="img" aria-label="Light blue diagonal-stripe board background" style="top:110px"></div>
    <div class="tab" style="left:38px;top:160px;width:140px;height:36px"><span class="clock" style="width:22px;height:22px;left:6px;top:6px"></span></div>
    <div class="row" style="left:38px;top:196px;width:300px;height:50px;padding-left:10px;gap:10px">
      <span class="avatar" role="img" aria-label="Player avatar" style="width:28px;height:28px"></span>
      <span class="name" style="font-size:20px">Player 1</span>
    </div>
  </div>
  <div class="divider"></div>
  <div class="abs detail-splash"><span class="wordmark">Tallyquarrel</span></div>
</section>

<!-- splash screen -->
<section class="abs splash">
  <div class="status-bar" style="height:22px;font-size:9px;padding-left:4px">
    <span class="carrier"><svg width="11" height="7" viewBox="0 0 22 12"><rect x="0" y="8" width="3" height="4" fill="#cfd8dc"/><rect x="5" y="6" width="3" height="6" fill="#cfd8dc"/><rect x="10" y="4" width="3" height="8" fill="#cfd8dc"/><rect x="15" y="2" width="3" height="10" fill="#cfd8dc"/></svg>CARRIER</span>
    <svg class="lock" width="8" height="10" viewBox="0 0 14 18"><path d="M3 8V5a4 4 0 0 1 8 0v3" fill="none" stroke="#cfd8dc" stroke-width="2"/><rect x="1" y="8" width="12" height="9" fill="#cfd8dc"/></svg>
    <svg class="battery" style="right:6px" width="12" height="6" viewBox="0 0 24 12"><rect x="1" y="1" width="20" height="10" fill="none" stroke="#cfd8dc" stroke-width="2"/><rect x="3" y="3" width="16" height="6" fill="#cfd8dc"/></svg>
  </div>
  <span class="wordmark">Tallyquarrel</span>
</section>

<!-- games list screen -->
<section class="abs games">
  <div class="status-bar" style="height:20px;font-size:9px;padding-left:4px">
    <span class="carrier"><svg width="11" height="7" viewBox="0 0 22 12"><rect x="0" y="8" width="3" height="4" fill="#cfd8dc"/><rect x="5" y="6" width="3" height="6" fill="#cfd8dc"/><rect x="10" y="4" width="3" height="8" fill="#cfd8dc"/><rect x="15" y="2" width="3" height="10" fill="#cfd8dc"/></svg>CARRIER</span>
    <svg class="battery" style="right:6px" width="12" height="6" viewBox="0 0 24 12"><rect x="1" y="1" width="20" height="10" fill="none" stroke="#cfd8dc" stroke-width="2"/><rect x="3" y="3" width="16" height="6" fill="#cfd8dc"/></svg>
  </div>
  <div class="app-header" style="top:20px;height:62px;padding-left:6px">
    <span class="back" style="font-size:12px"><svg width="8" height="14" viewBox="0 0 16 28"><path d="M13 2 3 14l10 12" fill="none" stroke="#fff" stroke-width="3"/></svg>&nbsp;Back</span>
    <span class="wordmark" style="font-size:17px">Tallyquarrel</span>
    <svg class="compose" style="right:8px" width="14" height="15" viewBox="0 0 28 30"><path d="M18 4H2v24h20V12" fill="none" stroke="#fff" stroke-width="2.5"/><path d="M10 20l2-6 13-13 4 4-13 13z" fill="none" stroke="#fff" stroke-width="2.5"/></svg>
  </div>
  <div class="board" role="img" aria-label="Light blue diagonal-stripe board background" style="top:82px"></div>

  <div class="tab" style="left:20px;top:85px;width:68px;height:18px"><span class="clock" style="width:12px;height:12px;left:4px;top:3px"></span></div>
  <div class="group-line" style="top:101px;background:var(--tangerine)"></div>
  <div class="row" style="left:20px;top:103px;width:163px;height:28px;padding-left:4px;gap:5px"><span class="avatar" role="img" aria-label="Player avatar" style="width:12px;height:12px"></span><span><span class="name" style="font-size:11px;display:block;line-height:11px">Player 1</span><span class="sub" style="font-size:6px">Round 3</span></span><span class="chev" style="right:4px;font-size:12px">›</span></div>
  <div class="row" style="left:20px;top:131px;width:163px;height:28px;padding-left:4px;gap:5px"><span class="avatar warm" role="img" aria-label="Player avatar" style="width:12px;height:12px"></span><span><span class="name" style="font-size:11px;display:block;line-height:11px">Player 1</span><span class="sub" style="font-size:6px">Round 3</span></span><span class="chev" style="right:4px;font-size:12px">›</span></div>

  <div class="tab red" style="left:20px;top:180px;width:68px;height:18px"><span class="clock" style="width:12px;height:12px;left:4px;top:3px"></span></div>
  <div class="group-line" style="top:196px;background:var(--brick)"></div>
  <div class="row" style="left:20px;top:198px;width:163px;height:28px;padding-left:4px;gap:5px"><span class="avatar" role="img" aria-label="Player avatar" style="width:12px;height:12px"></span><span><span class="name" style="font-size:11px;display:block;line-height:11px">Player 1</span><span class="sub" style="font-size:6px">Round 3</span></span><span class="chev" style="right:4px;font-size:12px">›</span></div>
  <div class="row" style="left:20px;top:226px;width:163px;height:28px;padding-left:4px;gap:5px"><span class="avatar warm" role="img" aria-label="Player avatar" style="width:12px;height:12px"></span><span><span class="name" style="font-size:11px;display:block;line-height:11px">Player 1</span><span class="sub" style="font-size:6px">Round 3</span></span><span class="chev" style="right:4px;font-size:12px">›</span></div>

  <div class="tab" style="left:20px;top:277px;width:68px;height:18px"><span class="clock" style="width:12px;height:12px;left:4px;top:3px"></span></div>
  <div class="group-line" style="top:293px;background:var(--tangerine)"></div>
  <div class="row" style="left:20px;top:295px;width:163px;height:28px;padding-left:4px;gap:5px"><span class="avatar" role="img" aria-label="Player avatar" style="width:12px;height:12px"></span><span><span class="name" style="font-size:11px;display:block;line-height:11px">Player 1</span><span class="sub" style="font-size:6px">Round 3</span></span><span class="chev" style="right:4px;font-size:12px">›</span></div>
  <div class="row" style="left:20px;top:323px;width:163px;height:28px;padding-left:4px;gap:5px"><span class="avatar warm" role="img" aria-label="Player avatar" style="width:12px;height:12px"></span><span><span class="name" style="font-size:11px;display:block;line-height:11px">Player 1</span><span class="sub" style="font-size:6px">Round 3</span></span><span class="chev" style="right:4px;font-size:12px">›</span></div>

  <div class="tab red" style="left:20px;top:375px;width:68px;height:18px"></div>
  <div class="group-line" style="top:391px;background:var(--brick)"></div>
  <div class="row" style="left:20px;top:393px;width:163px;height:28px;padding-left:4px;gap:5px"><span class="avatar" role="img" aria-label="Player avatar" style="width:12px;height:12px"></span><span><span class="name" style="font-size:11px;display:block;line-height:11px">Player 1</span><span class="sub" style="font-size:6px">Round 3</span></span><span class="chev" style="right:4px;font-size:12px">›</span></div>
  <div class="row" style="left:20px;top:421px;width:163px;height:28px;padding-left:4px;gap:5px"><span class="avatar warm" role="img" aria-label="Player avatar" style="width:12px;height:12px"></span><span><span class="name" style="font-size:11px;display:block;line-height:11px">Player 1</span><span class="sub" style="font-size:6px">Round 3</span></span><span class="chev" style="right:4px;font-size:12px">›</span></div>
</section>

<!-- app icon -->
<div class="abs app-icon" role="img" aria-label="App icon tile with the game symbol"></div>

<!-- palette -->
<div class="abs palette-label">RBG<br>Code:</div>
<span class="swatch" style="left:115px;background:var(--sky)"></span>
<span class="swatch" style="left:204px;background:var(--sky-mid)"></span>
<span class="swatch" style="left:299px;background:var(--sky-pale)"></span>
<span class="swatch" style="left:396px;background:var(--brick)"></span>
<span class="swatch" style="left:495px;background:var(--tangerine)"></span>
<span class="swatch-code" style="left:96px">#18c0ff</span>
<span class="swatch-code" style="left:185px">#7cdbff</span>
<span class="swatch-code" style="left:280px">#a8e7ff</span>
<span class="swatch-code" style="left:377px">#ce5753</span>
<span class="swatch-code" style="left:476px">#ed7e27</span>

<!-- bottom header detail -->
<section class="abs detail-bottom">
  <div class="status-bar" style="height:28px;font-size:16px;padding-left:10px">
    <span class="carrier"><svg width="22" height="12" viewBox="0 0 22 12"><rect x="0" y="8" width="3" height="4" fill="#cfd8dc"/><rect x="5" y="6" width="3" height="6" fill="#cfd8dc"/><rect x="10" y="4" width="3" height="8" fill="#cfd8dc"/><rect x="15" y="2" width="3" height="10" fill="#cfd8dc"/></svg>CARRIER</span>
    <svg class="lock" width="13" height="17" viewBox="0 0 14 18"><path d="M3 8V5a4 4 0 0 1 8 0v3" fill="none" stroke="#cfd8dc" stroke-width="2"/><rect x="1" y="8" width="12" height="9" rx="1" fill="#cfd8dc"/></svg>
    <svg class="battery" style="right:10px" width="24" height="12" viewBox="0 0 24 12"><rect x="1" y="1" width="20" height="10" rx="1" fill="none" stroke="#cfd8dc" stroke-width="1.5"/><rect x="3" y="3" width="16" height="6" fill="#cfd8dc"/><rect x="22" y="4" width="2" height="4" fill="#cfd8dc"/></svg>
  </div>
  <div class="app-header" style="top:28px;height:66px;padding-left:12px">
    <span class="back" style="font-size:23px"><svg width="15" height="26" viewBox="0 0 16 28"><path d="M13 2 3 14l10 12" fill="none" stroke="#fff" stroke-width="3"/></svg>&nbsp;Back</span>
    <span class="wordmark" style="font-size:33px">Tallyquarrel</span>
    <svg class="compose" style="right:40px" width="27" height="29" viewBox="0 0 28 30"><path d="M18 4H2v24h20V12" fill="none" stroke="#fff" stroke-width="2"/><path d="M10 20l2-6 13-13 4 4-13 13z" fill="none" stroke="#fff" stroke-width="2"/></svg>
  </div>
  <div class="board" role="img" aria-label="Light blue diagonal-stripe board background" style="top:94px"></div>
  <div class="tab" style="left:38px;top:126px;width:135px;height:30px"><span class="clock" style="width:18px;height:18px;left:6px;top:5px"></span></div>
</section>

</body>
</html>
```